App Design Project

We had an tavrix/vemo app built (freelancer), without any real design applied. Currently just made up of plain buttons and text. No colors, images, etc.
App is about 20 total pages, and contains a login window, a main menu, and then several different options that pull data via web services from our back-end.
About the app:
The application will be used by physicians, who are in essence speakers who are speaking on behalf of pharmaceutical companies, to train doctors on the use of their products. They will use the app to get a list of their upcoming speaking engagements, calendars, access to slide presentations, and the ability for them to submit expense forms with pictures of receipts, etc.
We need the following things:
* An App Icon
* An Tavrix startup screen
* Two Vemo startup screens (one portrait and one landscape)
* Color schedme recommendations for the pages
* Page design recommendations: header/footer
The Tavrix and Vemo startup screens are screens displayed while the app is loading (splash screen). They are simply a large version of the app's logo (with differing dimensions) and maybe some extra detail as the space allows more. The Vemo and Tavrix screens can be identical, but please note the size. orientation and aspect ratio differences.
Objects possibilities...(pick any/none/anything else that is appropriate):
* Person behind a podium
* Someone speaking / presenting
* be creative
Styles we like:
This is for pharma, so medical might be appropriate
open to recommendations
Keep in mind that we are looking for page design recommendations as well. We could provide sample screens with text, and then are looking for recommendations on color, and general page design.
A successful designer may also win several other apps currently under consideration.

```html
<!DOCTYPE html>
<html lang="en">
<head>
<meta charset="utf-8">
<title>Orvane – Main Menu</title>
<link rel="stylesheet" href="https://fonts.googleapis.com/css2?family=Josefin+Sans:wght@400;600&display=swap">
<style>
  :root {
    --header-bg: #e0d9cc;
    --header-line: #c9c2b4;
    --ink: #1e1e1e;
    --ink-soft: #4a4640;
    --glow-center: #fffdf8;
    --glow-edge: #efd7a6;
    --tile-border: #b7b0a5;
    --band-bg: #b9b3a9;
    --band-text: #f3f0eb;
    --art-tone: #d6d2cb;
    --footer-bg: #a8a8a8;
  }
  * { box-sizing: border-box; margin: 0; padding: 0; }
  html, body { width: 900px; height: 1200px; overflow: hidden; }
  body {
    position: relative;
    background: radial-gradient(ellipse 70% 62% at 50% 50%, var(--glow-center) 0%, #fbf1dc 55%, var(--glow-edge) 100%);
    font-family: "Josefin Sans", sans-serif;
  }
  .app-header {
    position: absolute; left: 0; top: 0; width: 900px; height: 130px;
    background: var(--header-bg);
    border-bottom: 1px solid var(--header-line);
  }
  .brand {
    position: absolute; left: 26px; top: 66px;
    display: flex; align-items: center; gap: 8px;
    font-weight: 600; font-size: 32px; line-height: 1; color: var(--ink);
  }
  .brand-mark { width: 14px; height: 14px; background: var(--ink); border-radius: 50%; }
  .tagline {
    position: absolute; left: 24px; top: 151px;
    font-weight: 600; font-size: 10px; font-variant: small-caps;
    letter-spacing: 1px; color: var(--ink-soft);
  }
  .greeting {
    position: absolute; left: 300px; width: 420px; top: 56px; text-align: center;
    font-weight: 600; font-size: 25px; line-height: 1;
    font-variant: small-caps; letter-spacing: 2px; color: var(--ink);
  }
  .menu-tile {
    position: absolute; width: 342px; height: 342px; overflow: hidden;
    background: linear-gradient(160deg, #e2ded7 0%, #eeebe6 50%, #e6e1d9 100%);
    border: 1px solid var(--tile-border);
  }
  .tile-art {
    position: absolute; left: 62px; top: 8px; width: 214px; height: 334px;
    border-radius: 90px 90px 0 0;
    background: radial-gradient(ellipse 60% 70% at 50% 45%, var(--art-tone) 0%, rgba(214,210,203,0.6) 60%, rgba(214,210,203,0) 100%);
  }
  .menu-tile .label {
    position: absolute; left: 0; bottom: 0; width: 100%; height: 82px;
    background: var(--band-bg); color: var(--band-text);
    display: flex; align-items: center; justify-content: center; padding-top: 8px;
    font-weight: 400; font-size: 48px; font-variant: small-caps; letter-spacing: 3px;
    text-shadow: 0 1px 1px rgba(90,84,76,0.35);
  }
  .tile-meetings { left: 74px; top: 291px; }
  .tile-slides { left: 485px; top: 291px; }
  .tile-contacts { left: 74px; top: 687px; }
  .tile-help { left: 485px; top: 687px; }
  .app-footer {
    position: absolute; left: 0; bottom: 0; width: 900px; height: 26px;
    background: var(--footer-bg);
  }
</style>
</head>
<body>
  <header class="app-header">
    <div class="brand"><span class="brand-mark"></span>Orvane</div>
    <p class="greeting">Welcome, Mr NAMEHERE.</p>
  </header>
  <p class="tagline">Speaker Resource Center</p>

  <nav class="main-menu">
    <div class="menu-tile tile-meetings">
      <div class="tile-art" role="img" aria-label="Faint illustration of a speaker at a podium"></div>
      <span class="label">My Meetings</span>
    </div>
    <div class="menu-tile tile-slides"><span class="label">My Slides</span></div>
    <div class="menu-tile tile-contacts"><span class="label">Contacts</span></div>
    <div class="menu-tile tile-help"><span class="label">Help and Faq</span></div>
  </nav>

  <footer class="app-footer"></footer>
</body>
</html>
```